Industry and Trade -may go complete production

Industrial and Corporate Clothing ecom and showcase web site
see supplier ref sites:
www.grondelgear.example.com.au
www.pellimarstitch.example.com/,
www.Qorwin.example.com.au
Our logo is a roundal shaped gear cog with an elephant inside it.
Main Objective

Get people to contact us for industrial and corporate wear
order online or contact us for more details on products

Information in seconday pages inmportant and ISO standards etc.
Primary Points:

Must show that we are strong and solid.
Visual imagery is important.
We have many web sites in line and this is a start, see bentmardispatch.example.com.au for one of ours.

We need a layout for the home page and internal pages. It's an ecomm retail site! Must sell the products AND our company.

Internal pages would be product description pages.

Each page must present an opportunity for them to contact us.
Updates

http://shop.zelkavision.example.com/clash-of-marrowdeep-a-fieldcraft-card-game/detail.php?p=471093&v=zkv_series_crowns-of-marrowdeep_games#tabs

has very good features 

Project Deadline Extended
Reason: Not Enough Responses. This will open up to a designer doing continuous designs for our company. We had lost our last in house designer and need a new innovative person to create genius.

Hi

This tender has been extended due to non response. 
This is our first look at the system as we had designers inder contract who have now left. There are may web sites etc to be done and this is more of a interview.

It is well worth responding. There are already 6 other projects in the pipline. But we want the best .
Garret de Vashmoor
Group COO Harbourline Dispatch Pty Ltd
Sydney Australia.

Target Market(s)

TARGET MARKET:
Tradesmen and Corporations and Government agencies
again see the above web sites they address the same markets
especially grondel.example.com.au

Industry/Entity Type

Industrial

Requirements
Must have
• Strength of company
supply and quality are important
ease of use, grondel.example.com.au can be used for good visual expression.
Nice to have
• extreme images and ease of use in navigation and contact.
look at imagery on grondel web site grondel.example.com.au
font useage: see http://money.quorvanews.example.com.au/newsbusiness/wpx/5139207/plendacom-signs-9b-fibre-agreement for font size usage. clear clean to the point.
Should not have
• kitch

```html
<!DOCTYPE html>
<html lang="en">
<head>
<meta charset="utf-8">
<title>Ferrowick Supply – Industrial and Corporate Clothing</title>
<link rel="stylesheet" href="https://fonts.googleapis.com/css2?family=Black+Ops+One&family=Arimo:wght@400;700&family=Share+Tech&display=swap">
<style>
:root{
  --red:#c8101a;
  --red-dark:#8e0a10;
  --ink:#222;
  --grey-text:#8a8a8a;
  --heading-grey:#6e6e6e;
  --panel:#ffffff;
  --frame:#d2d2d2;
  --band-dark:#1c1c1c;
  --page-edge:#6f6f6f;
  --footer:#3a3a3a;
}
*{box-sizing:border-box;margin:0;padding:0}
html,body{width:1200px;height:907px;overflow:hidden}
body{
  position:relative;
  font-family:"Arimo",Arial,sans-serif;
  background:linear-gradient(90deg,var(--page-edge) 0,#bdbdbd 2%,#f3f3f3 4%,#f3f3f3 96%,#bdbdbd 98%,var(--page-edge) 100%);
  color:var(--ink);
}
.abs{position:absolute}
a{text-decoration:none}

/* top utility bar */
.search-field{left:37px;top:34px;width:210px;height:20px;background:#fff;border:1px solid #bbb}
.search-btn{left:247px;top:34px;width:59px;height:20px;background:var(--red);color:#fff;font-size:13px;font-weight:700;text-align:center;line-height:20px}
.login-label{left:884px;font-size:13px;color:#222}
.login-field{left:976px;width:182px;height:18px;background:#fff;border:1px solid #aaa}

/* header band */
.header-band{left:34px;top:67px;width:1127px;height:106px;border-radius:14px;
  background:linear-gradient(180deg,#5a5a5a 0,var(--band-dark) 45%,#0d0d0d 70%,#3c3c3c 100%);
  box-shadow:0 3px 5px rgba(0,0,0,.4)}
.site-title{left:244px;top:84px;font-family:"Black Ops One",Impact,sans-serif;font-weight:400;color:#f4f4f4;white-space:nowrap}
.site-title .t1{font-size:40px;letter-spacing:1px}
.site-title .t2{font-size:34px;margin-left:28px}
.site-title .t3{font-size:58px;margin-left:26px;position:relative;top:-10px}

/* brand name */
.brand{left:48px;top:236px;width:230px;display:flex;align-items:center;gap:10px}
.brand-dot{width:34px;height:34px;border-radius:50%;background:#222;flex:none}
.brand-name{font-family:"Black Ops One",sans-serif;font-size:22px;line-height:24px;color:#222}

/* banner */
.banner-frame{left:300px;top:190px;width:858px;height:207px;border-radius:12px;background:#fff;
  border:1px solid #999;box-shadow:0 2px 5px rgba(0,0,0,.5);padding:5px}
.banner-photo{width:100%;height:100%;border-radius:9px;
  background:linear-gradient(90deg,#3a3a3a 0,#9a9a9a 18%,#c7c7c7 32%,#b24040 42%,#a8a8a8 56%,#5a5a5a 72%,#b07850 86%,#3a3a3a 100%)}
.sticker{left:850px;top:199px;width:122px;height:122px;border-radius:50%;
  background:radial-gradient(circle at 40% 35%,#e8262e,var(--red) 55%,var(--red-dark));
  box-shadow:0 3px 6px rgba(0,0,0,.5);color:#fff;font-family:"Black Ops One",sans-serif;font-size:40px;
  display:flex;align-items:center;justify-content:center;transform:rotate(-18deg)}

/* nav */
.main-nav{left:34px;top:411px;width:1127px;height:40px;border-radius:8px;
  background:linear-gradient(180deg,#6a6a6a,var(--band-dark) 50%,#2a2a2a);box-shadow:0 2px 4px rgba(0,0,0,.5)}
.nav-item{top:421px;font-family:"Black Ops One",sans-serif;font-size:18px;color:#fff;transform:translateX(-50%);white-space:nowrap}
.nav-item.current{color:var(--red)}

/* boxes */
.box{background:var(--panel);border:1px solid var(--frame)}
.badge{width:78px;height:78px;border-radius:50%;
  background:radial-gradient(circle at 40% 35%,#e8262e,var(--red) 60%,var(--red-dark));
  box-shadow:0 2px 4px rgba(0,0,0,.45);color:#fff;font-family:"Black Ops One",sans-serif;
  display:flex;align-items:center;justify-content:center;text-align:center;line-height:1;font-size:17px}
.small-text{font-size:11.5px;color:var(--grey-text);line-height:14px}
.box-title{font-size:16px;color:var(--heading-grey)}

/* content */
.content-heading{left:295px;font-family:"Black Ops One",sans-serif;font-weight:400;font-size:27px;color:var(--heading-grey);letter-spacing:1px}
.content-body{left:295px;width:624px;font-family:"Share Tech",Arial,sans-serif;font-size:13.4px;line-height:15.5px;color:var(--grey-text)}

.cta-bar{background:var(--red);color:#fff;font-size:11px;font-weight:700;line-height:13px;padding:2px 6px}
.enews-title{color:var(--red);font-weight:700;font-size:16px;text-align:center}
.social-row{height:24px;border:1px solid #ccc;background:#f7f7f7;font-size:12px;color:var(--grey-text);
  display:flex;align-items:center}
.social-row .mark{width:20px;height:20px;margin:0 10px 0 6px;background:var(--grey-text)}
.social-row span{flex:1;text-align:center}

.footer{left:0;top:877px;width:1200px;height:30px;background:var(--footer);color:#ddd;font-size:10px}
</style>
</head>
<body>

<div class="abs search-field"></div>
<div class="abs search-btn">Search</div>
<div class="abs login-label" style="top:20px">Login</div>
<div class="abs login-label" style="top:38px">User name</div>
<div class="abs login-field" style="top:18px"></div>
<div class="abs login-field" style="top:38px"></div>

<header>
  <div class="abs header-band"></div>
  <h1 class="abs site-title"><span class="t1">Industrial</span><span class="t2">and Corporate</span><span class="t3">clothing</span></h1>

  <div class="abs brand"><span class="brand-dot"></span><span class="brand-name">Ferrowick Supply</span></div>

  <div class="abs banner-frame"><div class="banner-photo" role="img" aria-label="Photo of two workers in red overalls and hard hats inspecting large steel pipes"></div></div>
  <div class="abs sticker">10%</div>
</header>

<nav>
  <div class="abs main-nav"></div>
  <a class="abs nav-item" style="left:101px">Home</a>
  <a class="abs nav-item" style="left:236px">Services</a>
  <a class="abs nav-item" style="left:390px">Products</a>
  <a class="abs nav-item" style="left:542px">About us</a>
  <a class="abs nav-item" style="left:678px">FAQs</a>
  <a class="abs nav-item" style="left:816px">Materials</a>
  <a class="abs nav-item current" style="left:971px">Contact</a>
  <a class="abs nav-item" style="left:1099px">Shop</a>
</nav>

<section class="abs box" style="left:37px;top:464px;width:232px;height:202px">
  <div class="abs badge" style="left:14px;top:0">News</div>
  <div class="abs small-text" style="left:10px;top:80px;font-size:14px">12.06.2011</div>
  <div class="abs box-title" style="left:10px;top:98px">Quisque vitae pede.</div>
  <p class="abs small-text" style="left:10px;top:122px;width:212px">Quisque vitae pede. Nam et augue. Sed a elit. Ut vel massa. Suspendisse nibh pede, ultrices vitae,ultrices nec, mollis non nibh...</p>
  <div class="abs small-text" style="right:12px;top:182px">Learn more...</div>
</section>

<section class="abs box" style="left:37px;top:683px;width:232px;height:178px">
  <div class="abs badge" style="left:14px;top:2px">Buy<br>now</div>
  <div class="abs" role="img" aria-label="Navy and yellow hi-vis work jacket" style="left:20px;top:80px;width:84px;height:84px;border:1px solid #ccc;background:linear-gradient(160deg,#2b3f7a,#1d2a55 60%,#d9c21a)"></div>
  <div class="abs" role="img" aria-label="Navy and grey work jacket" style="left:122px;top:80px;width:84px;height:84px;border:1px solid #ccc;background:linear-gradient(160deg,#2c3a63,#555b66 60%,#9a3030)"></div>
</section>

<h2 class="abs content-heading" style="top:460px">Quisque vitae pede.</h2>
<p class="abs content-body" style="top:498px">Quisque vitae pede. Nam et augue. Sed a elit. Ut vel massa. Suspendisse nibh pede, ultrices vitae, ultrices nec, mollis non nibh.Quisque vitae pede. Nam et augue. Sed a elit. Ut vel massa. Suspendisse nibh pede, ultrices vitae,ultrices nec, mollis non nibh. Quisque vitae pede. Nam et augue. Sed a elit. Ut vel massa. Suspendisse nibh pede, ultrices vitae ultrices nec, mollis non nibh. Quisque vitae pede. Nam et augue. Sed a elit. Ut vel massa. Suspendisse nibh pede, ultrices vitae ultrices nec, mollis non nibh... Quisque vitae pede. Nam et augue. Sed a elit. Ut vel massa. Suspendisse nibh pede, ultrices vitae ultrices nec, mollis non nibh... Suspendisse nibh pede, ultrices vitae ultrices nec, mollis non nibh...</p>

<h2 class="abs content-heading" style="top:644px">Quisque vitae pede.</h2>
<p class="abs content-body" style="top:684px">Quisque vitae pede. Nam et augue. Sed a elit. Ut vel massa. Suspendisse nibh pede, ultrices vitae, ultrices nec, mollis non nibh.Quisque vitae pede. Nam et augue. Sed a elit. Ut vel massa. Suspendisse nibh pede, ultrices vitae,ultrices nec, mollis non nibh. Quisque vitae pede. Nam et augue. Sed a elit. Ut vel massa. Suspendisse nibh pede, ultrices vitae ultrices nec, mollis non nibh. Quisque vitae pede. Nam et augue. Sed a elit. Ut vel massa. Suspendisse nibh pede, ultrices vitae ultrices nec, mollis non nibh... Quisque vitae pede. Nam et augue. Sed a elit. Ut vel massa. Suspendisse nibh pede, ultrices vitae ultrices nec, mollis non nibh... Suspendisse nibh pede, ultrices vitae ultrices nec, mollis non nibh...</p>
<p class="abs content-body" style="top:823px">Suspendisse nibh pede, ultrices vitae ultrices nec, mollis non nibh... Suspendisse nibh pede, ultrices vitae ultrices nec, mollis non nibh...</p>

<section class="abs box" style="left:939px;top:464px;width:219px;height:197px">
  <div class="abs badge" style="left:18px;top:0;font-size:13px;transform:rotate(-20deg)">Request<br>a<br>Quote</div>
  <div class="abs box-title" style="left:12px;top:82px;font-size:15px">Quisque vitae pede.</div>
  <p class="abs small-text" style="left:12px;top:100px;width:200px;font-size:11px;line-height:12.5px">Quisque vitae pede. Nam et augue. Sed a elit. Ut vel massa. Suspendisse nibh pede, ultrices vitae,ultrices nec, mollis non nibh...</p>
  <div class="abs cta-bar" style="left:8px;top:160px;width:202px">Contact us for a no obligation free quote.</div>
</section>

<section class="abs box" style="left:939px;top:682px;width:219px;height:177px">
  <div class="abs enews-title" style="left:0;top:2px;width:219px">eNews sign up</div>
  <div class="abs" style="left:6px;top:22px;width:174px;height:22px;border:1px solid #aaa;font-size:14px;line-height:20px;padding-left:4px">Your email</div>
  <div class="abs" style="left:182px;top:22px;width:30px;height:22px;background:var(--red);color:#fff;font-weight:700;font-size:13px;text-align:center;line-height:22px">Go</div>
  <div class="abs social-row" style="left:6px;top:50px;width:206px"><i class="mark"></i><span>like us on Friendlane</span></div>
  <div class="abs social-row" style="left:6px;top:77px;width:206px"><i class="mark"></i><span>follow us on Chirpline</span></div>
  <div class="abs social-row" style="left:6px;top:104px;width:206px"><i class="mark"></i><span>subscribe to rss feed</span></div>
  <div class="abs" style="left:6px;top:132px;width:206px;height:26px;background:linear-gradient(#e0262e,var(--red-dark));color:#fff;font-weight:700;font-size:15px;text-align:center;line-height:26px;border-radius:3px">eNews Letter</div>
</section>

<footer class="abs footer">
  <div class="abs" style="left:46px;top:10px">Copyright ©2011 All rights reserved</div>
  <div class="abs" style="left:962px;top:10px">Contact us &nbsp;|&nbsp; Terms and Conditions &nbsp;|&nbsp; Site map</div>
</footer>

</body>
</html>
```